MARLOWE THREADWORK WEB DESIGN PROJECT

We are a brand new company called "Marlowe Threadwork" which specialise in one-off Vintage Clothing. We would like somebody to design a web page which will be the sole income for our company. Our main aim is to have an easy searchable website which is user friendly. The key to the website is to target people who do not like the idea of op-shopping but love vintage clothes - this website will be the answer.
Updates

This website will need to be coded to work with Halvo Shopdesk - Please read this before you start. https://help.halvoshopdesk.example/articles/Public/How-do-I-create-custom-template-files-for-my-store

Hi everyone, Just want to make note that the this website is for young people. Just so people a clear I want modern young people dressed in Vintage clothes as this is that reality and what they would like to see. Not people dressed like they are going to a fancy dress party, i.e. dresses like it was that era. Thanks Rosalind

Coding

Coded - Design and coding required

```html
<!DOCTYPE html>
<html lang="en">
<head>
<meta charset="utf-8">
<title>Marlowe Threadwork – Vintage Dresses</title>
<link href="https://fonts.googleapis.com/css2?family=Montserrat:wght@600;700&family=Roboto:wght@300;400;500&family=Roboto+Condensed:wght@400&display=swap" rel="stylesheet">
<style>
:root{
  --pink:#f0548e;
  --pink-soft:#f27aa6;
  --teal:#3ec6c6;
  --heading:#1d7a9a;
  --ink:#222;
  --text:#555;
  --muted:#999;
  --line:#ddd;
  --bar:#ececec;
  --band:#efefef;
  --footer:#f4f4f4;
  --white:#fff;
}
*{box-sizing:border-box;margin:0;padding:0}
html,body{width:1200px;height:2579px;overflow:hidden;background:var(--white)}
body{position:relative;font-family:"Roboto",Arial,sans-serif;color:var(--text)}
a{color:inherit;text-decoration:none}
.abs{position:absolute}

/* top bar */
.topbar{left:0;top:0;width:1200px;height:43px;background:var(--bar);font-size:12px;color:#444}
.topbar .tag{left:92px;top:15px}
.topbar .util{right:92px;top:15px;display:flex;gap:10px}
.topbar .util span.sep{color:#888}

/* header */
.brand{left:88px;top:66px}
.brand-name{font-family:"Montserrat",sans-serif;font-weight:700;font-size:32px;color:var(--pink);letter-spacing:1px;line-height:1}
.brand-sub{font-family:"Montserrat",sans-serif;font-weight:600;font-size:17px;color:var(--ink);margin-top:6px}
.search{left:598px;top:72px;width:282px;height:43px;border:2px solid #ccc;border-right:none;border-radius:3px 0 0 3px;display:flex}
.search input{border:none;font-size:11px;padding-left:12px;width:240px;color:#888;font-family:inherit;background:transparent}
.search-btn{left:843px;top:72px;width:38px;height:43px;background:var(--pink);border-radius:0 3px 3px 0;display:flex;align-items:center;justify-content:center}
.member{left:929px;top:52px;font-size:10px;color:#333;line-height:1.35;padding-left:26px}
.member b{color:var(--pink);font-weight:400}
.member svg{position:absolute;left:0;top:4px}
.btn-join,.btn-login{top:84px;height:31px;border-radius:3px;color:var(--white);font-size:15px;display:flex;align-items:center;justify-content:center}
.btn-join{left:927px;width:86px;background:var(--teal)}
.btn-login{left:1026px;width:85px;background:var(--pink)}

/* nav */
.nav{left:88px;top:155px;width:722px;height:50px;border-top:2px solid var(--pink);border-bottom:3px solid var(--pink);display:flex;align-items:center;font-size:17px;font-weight:500;color:var(--ink)}
.nav .home{margin-left:14px;margin-right:34px;display:flex}
.nav .women{margin-right:63px}
.nav .tools{margin-left:auto;display:flex;gap:22px;font-size:12px;margin-right:22px}
.nav .tools span{display:flex;align-items:center;gap:6px}
.promo{left:810px;top:155px;width:304px;height:51px;background:var(--teal);color:var(--white);text-align:center;padding-top:9px}
.promo strong{display:block;font-size:13px;font-weight:500}
.promo small{display:block;font-size:10px;margin-top:3px}

/* sidebar */
.filter{left:88px;width:247px;border:1px solid #cfcfcf;box-shadow:0 2px 4px rgba(0,0,0,.15);padding:24px 0 0 21px;background:var(--white)}
.filter h3{font-size:17px;font-weight:500;color:var(--heading);width:186px;border-bottom:1px solid #aaa;padding-bottom:5px;margin-bottom:8px}
.filter ul{list-style:none}
.filter li{display:flex;align-items:center;gap:12px;font-size:14px;color:#555;height:31px}
.filter li i{width:16px;height:16px;border:1px solid #aaa;display:block}
.filter .more{font-size:9px;color:var(--pink);text-decoration:underline;margin-left:4px;display:block;margin-top:-2px}

/* main */
.crumbs{left:352px;top:235px;font-size:14px;color:#555}
.page-title{left:352px;top:266px;font-size:25px;font-weight:500;color:var(--pink)}
.intro{left:352px;top:306px;width:750px;font-size:13px;line-height:22px;color:#555}
.grid{left:352px;top:370px;width:762px;display:grid;grid-template-columns:repeat(3,233px);column-gap:31px;row-gap:27px}
.card .photo{height:240px}
.card .caption{height:31px;background:#ececec;font-size:16px;color:#444;display:flex;align-items:center;justify-content:center}
.card .price{text-align:center;margin-top:12px;font-family:"Roboto Condensed",sans-serif;font-size:19px;color:#222}
.card .price s{font-size:13px;color:var(--muted);margin-right:5px}
.card .actions{margin-top:10px;display:grid;grid-template-columns:repeat(4,1fr);border:1px solid var(--line);height:40px}
.card .actions span{display:flex;align-items:center;justify-content:center;border-left:1px solid var(--line)}
.card .actions span:first-child{border-left:none}
.card .actions .on{background:var(--pink)}

/* newsletter */
.community{left:88px;top:1936px;width:1026px;height:190px;background:radial-gradient(ellipse at 50% 40%,#fafafa,#e6e6e6)}
.community h2{position:absolute;left:35px;top:32px;font-size:21px;font-weight:400;color:#222}
.community p{position:absolute;left:35px;top:62px;font-size:16px;color:var(--pink)}
.community .field{position:absolute;left:35px;top:95px;width:423px;height:55px;border:2px solid #ccc;background:var(--white);box-shadow:inset 0 1px 3px rgba(0,0,0,.1)}
.community .subscribe{position:absolute;left:461px;top:95px;width:140px;height:55px;background:var(--pink);color:var(--white);font-size:16px;font-weight:500;display:flex;align-items:center;justify-content:center;border-radius:2px}
.community h4{position:absolute;left:665px;top:32px;font-size:21px;font-weight:400;color:#222}
.social{position:absolute;top:70px;display:flex;flex-direction:column;align-items:center;gap:6px;font-size:11px;color:#444}
.social i{display:block;width:50px;height:50px;border-radius:50%;border:3px solid var(--white);box-shadow:0 2px 4px rgba(0,0,0,.3)}

/* footer */
.footer{left:88px;top:2126px;width:1026px;height:453px;background:var(--footer)}
.fcol{position:absolute;top:40px}
.fcol h5{font-size:15px;font-weight:400;color:var(--pink);margin-bottom:18px}
.fcol li{list-style:none;font-size:14px;color:#333;height:26px}
.fcol.cats ul{display:grid;grid-template-columns:130px 60px;row-gap:9px}
.fcol.cats li{height:26px}
.partners{position:absolute;top:300px;left:45px;width:936px;display:flex;justify-content:space-between;align-items:center}
.partner{display:flex;align-items:center;gap:10px;font-size:26px;font-weight:500;color:#333}
.partner i{display:block;width:30px;height:30px}
.copyright{position:absolute;left:0;width:100%;top:400px;text-align:center;font-size:12px;color:#333}
</style>
</head>
<body>

<div class="abs topbar">
  <span class="abs tag">Australian Owned and Operated</span>
  <nav class="abs util"><a>View Cart</a><span class="sep">|</span><a>Wish List</a><span class="sep">|</span><a>Help</a></nav>
</div>

<header>
  <div class="abs brand">
    <div class="brand-name">MARLOWE THREADWORK</div>
    <div class="brand-sub">Unique Vintage Fashion and Accessories</div>
  </div>
  <div class="abs search"><input type="text" placeholder="Search one off vintage items..."></div>
  <div class="abs search-btn"><svg width="16" height="16" viewBox="0 0 16 16"><circle cx="6.5" cy="6.5" r="4.5" fill="none" stroke="#fff" stroke-width="2"/><line x1="10" y1="10" x2="14" y2="14" stroke="#fff" stroke-width="2.4" stroke-linecap="round"/></svg></div>
  <div class="abs member">
    <svg width="18" height="14" viewBox="0 0 18 14"><path d="M2 13 Q3 4 13 4" fill="none" stroke="#3ec6c6" stroke-width="2"/><path d="M11 0 L17 4 L11 8 Z" fill="#3ec6c6"/></svg>
    Become a member and receive a<br><b>5%</b> discount
  </div>
  <a class="abs btn-join">Sign Up</a>
  <a class="abs btn-login">Log In</a>
</header>

<nav class="abs nav">
  <span class="home"><svg width="24" height="20" viewBox="0 0 24 20"><path d="M12 1 L23 10 H20 V19 H14 V13 H10 V19 H4 V10 H1 Z" fill="#f0548e"/></svg></span>
  <span class="women">WOMEN</span>
  <span>MEN</span>
  <span class="tools">
    <span><svg width="18" height="18" viewBox="0 0 18 18"><path d="M2 2 L16 16 M16 2 L2 16" stroke="#222" stroke-width="3"/></svg>STYLE TIPS</span>
    <span><svg width="18" height="18" viewBox="0 0 18 18"><circle cx="9" cy="9" r="8" fill="#222"/><text x="9" y="13" text-anchor="middle" font-size="11" font-weight="700" fill="#fff" font-family="Roboto,sans-serif">?</text></svg>FAQS</span>
  </span>
</nav>
<div class="abs promo"><strong>Orders over $100 will receive FREE shipping!</strong><small>Find out more about delivery &amp; shipping &gt;&gt;&gt;</small></div>

<aside>
  <section class="abs filter" style="top:234px;height:196px"><h3>Vintage Clothes</h3><ul><li><i></i>Dresses (100)</li><li><i></i>Shirts &amp; T-Shirts (50)</li><li><i></i>Shorts (40)</li></ul><a class="more">See More..</a></section>
  <section class="abs filter" style="top:452px;height:215px"><h3>Era</h3><ul><li><i></i>1950s</li><li><i></i>1960s</li><li><i></i>1970s</li><li><i></i>1980s</li></ul><a class="more">See More..</a></section>
  <section class="abs filter" style="top:689px;height:241px"><h3>Size</h3><ul><li><i></i>Six</li><li><i></i>Eight</li><li><i></i>Ten</li><li><i></i>Twelve</li><li><i></i>Fourteen</li></ul><a class="more">See More..</a></section>
  <section class="abs filter" style="top:954px;height:181px"><h3>Colour</h3><ul><li><i></i>Black</li><li><i></i>White</li><li><i></i>Red</li></ul><a class="more">See More..</a></section>
  <section class="abs filter" style="top:1159px;height:187px"><h3>Pattern</h3><ul><li><i></i>Poke-a-dot</li><li><i></i>Floral</li><li><i></i>Stripes</li></ul><a class="more">See More..</a></section>
  <section class="abs filter" style="top:1372px;height:163px"><h3>Brand</h3><ul><li><i></i>xyz</li><li><i></i>xyz</li></ul><a class="more">See More..</a></section>
  <section class="abs filter" style="top:1570px;height:316px"><h3>Price</h3><ul><li><i></i>$10-15</li><li><i></i>$15-$20</li><li><i></i>$20-$30</li><li><i></i>$30-$40</li><li><i></i>$40-$50</li><li><i></i>$50-$100</li><li><i></i>$100+</li></ul><a class="more">See More..</a></section>
</aside>

<main>
  <div class="abs crumbs">Home &gt;&nbsp;&nbsp;&nbsp; Women &gt; Dresses</div>
  <h1 class="abs page-title">VINTAGE DRESSES</h1>
  <p class="abs intro">All our dresses are one-off vintage pieces – and are all pre-loved. However all our clothes are in mint-condition and will look as though they are brand new. Be quick, as there is only one available per item and will disappear from the web once sold!</p>

  <div class="abs grid">
    <!-- product cards -->
    <article class="card"><div class="photo" role="img" aria-label="Model in a mint green vintage sundress" style="background:radial-gradient(ellipse 35% 55% at 50% 58%,#8fdcc8,#e6e6e6 95%)"></div><div class="caption">Lorem ipsum dolor</div><div class="price"><s>$160.00</s>$150.00</div><div class="actions"><span class="on"><svg width="16" height="14" viewBox="0 0 16 14"><path d="M1 1 H3 L5 9 H13 L15 3 H4" fill="none" stroke="#fff" stroke-width="1.6"/><circle cx="6" cy="12" r="1.3" fill="#fff"/><circle cx="12" cy="12" r="1.3" fill="#fff"/></svg></span><span><svg width="14" height="13" viewBox="0 0 14 13"><path d="M7 12 L1.5 6.5 A3 3 0 0 1 7 2.5 A3 3 0 0 1 12.5 6.5 Z" fill="#bbb"/></svg></span><span><svg width="16" height="12" viewBox="0 0 16 12"><path d="M1 3 H13 M10 0 L13 3 L10 6 M15 9 H3 M6 6 L3 9 L6 12" fill="none" stroke="#bbb" stroke-width="1.6"/></svg></span><span><svg width="14" height="14" viewBox="0 0 14 14"><circle cx="7" cy="7" r="6" fill="none" stroke="#bbb" stroke-width="1.4"/><path d="M7 4 V7 H9" fill="none" stroke="#bbb" stroke-width="1.4"/></svg></span></div></article>
    <article class="card"><div class="photo" role="img" aria-label="Model in a teal satin vintage dress" style="background:radial-gradient(ellipse 35% 55% at 50% 58%,#1f8f8a,#e6e6e6 95%)"></div><div class="caption">Lorem ipsum dolor</div><div class="price"><s>$160.00</s>$150.00</div><div class="actions"><span><svg width="16" height="14" viewBox="0 0 16 14"><path d="M1 1 H3 L5 9 H13 L15 3 H4" fill="none" stroke="#bbb" stroke-width="1.6"/><circle cx="6" cy="12" r="1.3" fill="#bbb"/><circle cx="12" cy="12" r="1.3" fill="#bbb"/></svg></span><span><svg width="14" height="13" viewBox="0 0 14 13"><path d="M7 12 L1.5 6.5 A3 3 0 0 1 7 2.5 A3 3 0 0 1 12.5 6.5 Z" fill="#bbb"/></svg></span><span><svg width="16" height="12" viewBox="0 0 16 12"><path d="M1 3 H13 M10 0 L13 3 L10 6 M15 9 H3 M6 6 L3 9 L6 12" fill="none" stroke="#bbb" stroke-width="1.6"/></svg></span><span><svg width="14" height="14" viewBox="0 0 14 14"><circle cx="7" cy="7" r="6" fill="none" stroke="#bbb" stroke-width="1.4"/><path d="M7 4 V7 H9" fill="none" stroke="#bbb" stroke-width="1.4"/></svg></span></div></article>
    <article class="card"><div class="photo" role="img" aria-label="Model in a blue and white patterned vintage dress" style="background:radial-gradient(ellipse 35% 55% at 50% 58%,#6f8fd6,#e6e6e6 95%)"></div><div class="caption">Lorem ipsum dolor</div><div class="price"><s>$160.00</s>$150.00</div><div class="actions"><span><svg width="16" height="14" viewBox="0 0 16 14"><path d="M1 1 H3 L5 9 H13 L15 3 H4" fill="none" stroke="#bbb" stroke-width="1.6"/><circle cx="6" cy="12" r="1.3" fill="#bbb"/><circle cx="12" cy="12" r="1.3" fill="#bbb"/></svg></span><span><svg width="14" height="13" viewBox="0 0 14 13"><path d="M7 12 L1.5 6.5 A3 3 0 0 1 7 2.5 A3 3 0 0 1 12.5 6.5 Z" fill="#bbb"/></svg></span><span><svg width="16" height="12" viewBox="0 0 16 12"><path d="M1 3 H13 M10 0 L13 3 L10 6 M15 9 H3 M6 6 L3 9 L6 12" fill="none" stroke="#bbb" stroke-width="1.6"/></svg></span><span><svg width="14" height="14" viewBox="0 0 14 14"><circle cx="7" cy="7" r="6" fill="none" stroke="#bbb" stroke-width="1.4"/><path d="M7 4 V7 H9" fill="none" stroke="#bbb" stroke-width="1.4"/></svg></span></div></article>

    <article class="card"><div class="photo" role="img" aria-label="Model in a red cardigan and black jeans" style="background:radial-gradient(ellipse 35% 55% at 50% 58%,#a3263a,#e6e6e6 95%)"></div><div class="caption">Lorem ipsum dolor</div><div class="price"><s>$160.00</s>$150.00</div><div class="actions"><span><svg width="16" height="14" viewBox="0 0 16 14"><path d="M1 1 H3 L5 9 H13 L15 3 H4" fill="none" stroke="#bbb" stroke-width="1.6"/><circle cx="6" cy="12" r="1.3" fill="#bbb"/><circle cx="12" cy="12" r="1.3" fill="#bbb"/></svg></span><span><svg width="14" height="13" viewBox="0 0 14 13"><path d="M7 12 L1.5 6.5 A3 3 0 0 1 7 2.5 A3 3 0 0 1 12.5 6.5 Z" fill="#bbb"/></svg></span><span><svg width="16" height="12" viewBox="0 0 16 12"><path d="M1 3 H13 M10 0 L13 3 L10 6 M15 9 H3 M6 6 L3 9 L6 12" fill="none" stroke="#bbb" stroke-width="1.6"/></svg></span><span><svg width="14" height="14" viewBox="0 0 14 14"><circle cx="7" cy="7" r="6" fill="none" stroke="#bbb" stroke-width="1.4"/><path d="M7 4 V7 H9" fill="none" stroke="#bbb" stroke-width="1.4"/></svg></span></div></article>
    <article class="card"><div class="photo" role="img" aria-label="Model in a black floral print vintage dress" style="background:radial-gradient(ellipse 35% 55% at 50% 58%,#2a2a32,#e6e6e6 95%)"></div><div class="caption">Lorem ipsum dolor</div><div class="price"><s>$160.00</s>$150.00</div><div class="actions"><span><svg width="16" height="14" viewBox="0 0 16 14"><path d="M1 1 H3 L5 9 H13 L15 3 H4" fill="none" stroke="#bbb" stroke-width="1.6"/><circle cx="6" cy="12" r="1.3" fill="#bbb"/><circle cx="12" cy="12" r="1.3" fill="#bbb"/></svg></span><span><svg width="14" height="13" viewBox="0 0 14 13"><path d="M7 12 L1.5 6.5 A3 3 0 0 1 7 2.5 A3 3 0 0 1 12.5 6.5 Z" fill="#bbb"/></svg></span><span><svg width="16" height="12" viewBox="0 0 16 12"><path d="M1 3 H13 M10 0 L13 3 L10 6 M15 9 H3 M6 6 L3 9 L6 12" fill="none" stroke="#bbb" stroke-width="1.6"/></svg></span><span><svg width="14" height="14" viewBox="0 0 14 14"><circle cx="7" cy="7" r="6" fill="none" stroke="#bbb" stroke-width="1.4"/><path d="M7 4 V7 H9" fill="none" stroke="#bbb" stroke-width="1.4"/></svg></span></div></article>
    <article class="card"><div class="photo" role="img" aria-label="Model in a black top with white collar and black trousers" style="background:radial-gradient(ellipse 35% 55% at 50% 58%,#1e1e22,#e6e6e6 95%)"></div><div class="caption">Lorem ipsum dolor</div><div class="price"><s>$160.00</s>$150.00</div><div class="actions"><span><svg width="16" height="14" viewBox="0 0 16 14"><path d="M1 1 H3 L5 9 H13 L15 3 H4" fill="none" stroke="#bbb" stroke-width="1.6"/><circle cx="6" cy="12" r="1.3" fill="#bbb"/><circle cx="12" cy="12" r="1.3" fill="#bbb"/></svg></span><span><svg width="14" height="13" viewBox="0 0 14 13"><path d="M7 12 L1.5 6.5 A3 3 0 0 1 7 2.5 A3 3 0 0 1 12.5 6.5 Z" fill="#bbb"/></svg></span><span><svg width="16" height="12" viewBox="0 0 16 12"><path d="M1 3 H13 M10 0 L13 3 L10 6 M15 9 H3 M6 6 L3 9 L6 12" fill="none" stroke="#bbb" stroke-width="1.6"/></svg></span><span><svg width="14" height="14" viewBox="0 0 14 14"><circle cx="7" cy="7" r="6" fill="none" stroke="#bbb" stroke-width="1.4"/><path d="M7 4 V7 H9" fill="none" stroke="#bbb" stroke-width="1.4"/></svg></span></div></article>

    <article class="card"><div class="photo" role="img" aria-label="Model in a black dress with red cherry print" style="background:radial-gradient(ellipse 35% 55% at 50% 58%,#5a1a1e,#e6e6e6 95%)"></div><div class="caption">Lorem ipsum dolor</div><div class="price"><s>$160.00</s>$150.00</div><div class="actions"><span><svg width="16" height="14" viewBox="0 0 16 14"><path d="M1 1 H3 L5 9 H13 L15 3 H4" fill="none" stroke="#bbb" stroke-width="1.6"/><circle cx="6" cy="12" r="1.3" fill="#bbb"/><circle cx="12" cy="12" r="1.3" fill="#bbb"/></svg></span><span><svg width="14" height="13" viewBox="0 0 14 13"><path d="M7 12 L1.5 6.5 A3 3 0 0 1 7 2.5 A3 3 0 0 1 12.5 6.5 Z" fill="#bbb"/></svg></span><span><svg width="16" height="12" viewBox="0 0 16 12"><path d="M1 3 H13 M10 0 L13 3 L10 6 M15 9 H3 M6 6 L3 9 L6 12" fill="none" stroke="#bbb" stroke-width="1.6"/></svg></span><span><svg width="14" height="14" viewBox="0 0 14 14"><circle cx="7" cy="7" r="6" fill="none" stroke="#bbb" stroke-width="1.4"/><path d="M7 4 V7 H9" fill="none" stroke="#bbb" stroke-width="1.4"/></svg></span></div></article>
    <article class="card"><div class="photo" role="img" aria-label="Model in a black vintage dress holding a red handbag" style="background:radial-gradient(ellipse 35% 55% at 50% 58%,#26262a,#e6e6e6 95%)"></div><div class="caption">Lorem ipsum dolor</div><div class="price"><s>$160.00</s>$150.00</div><div class="actions"><span><svg width="16" height="14" viewBox="0 0 16 14"><path d="M1 1 H3 L5 9 H13 L15 3 H4" fill="none" stroke="#bbb" stroke-width="1.6"/><circle cx="6" cy="12" r="1.3" fill="#bbb"/><circle cx="12" cy="12" r="1.3" fill="#bbb"/></svg></span><span><svg width="14" height="13" viewBox="0 0 14 13"><path d="M7 12 L1.5 6.5 A3 3 0 0 1 7 2.5 A3 3 0 0 1 12.5 6.5 Z" fill="#bbb"/></svg></span><span><svg width="16" height="12" viewBox="0 0 16 12"><path d="M1 3 H13 M10 0 L13 3 L10 6 M15 9 H3 M6 6 L3 9 L6 12" fill="none" stroke="#bbb" stroke-width="1.6"/></svg></span><span><svg width="14" height="14" viewBox="0 0 14 14"><circle cx="7" cy="7" r="6" fill="none" stroke="#bbb" stroke-width="1.4"/><path d="M7 4 V7 H9" fill="none" stroke="#bbb" stroke-width="1.4"/></svg></span></div></article>
    <article class="card"><div class="photo" role="img" aria-label="Model in a grey and black patterned halter dress" style="background:radial-gradient(ellipse 35% 55% at 50% 58%,#5c5c62,#e6e6e6 95%)"></div><div class="caption">Lorem ipsum dolor</div><div class="price"><s>$160.00</s>$150.00</div><div class="actions"><span><svg width="16" height="14" viewBox="0 0 16 14"><path d="M1 1 H3 L5 9 H13 L15 3 H4" fill="none" stroke="#bbb" stroke-width="1.6"/><circle cx="6" cy="12" r="1.3" fill="#bbb"/><circle cx="12" cy="12" r="1.3" fill="#bbb"/></svg></span><span><svg width="14" height="13" viewBox="0 0 14 13"><path d="M7 12 L1.5 6.5 A3 3 0 0 1 7 2.5 A3 3 0 0 1 12.5 6.5 Z" fill="#bbb"/></svg></span><span><svg width="16" height="12" viewBox="0 0 16 12"><path d="M1 3 H13 M10 0 L13 3 L10 6 M15 9 H3 M6 6 L3 9 L6 12" fill="none" stroke="#bbb" stroke-width="1.6"/></svg></span><span><svg width="14" height="14" viewBox="0 0 14 14"><circle cx="7" cy="7" r="6" fill="none" stroke="#bbb" stroke-width="1.4"/><path d="M7 4 V7 H9" fill="none" stroke="#bbb" stroke-width="1.4"/></svg></span></div></article>

    <article class="card"><div class="photo" role="img" aria-label="Model in a burgundy lace vintage dress" style="background:radial-gradient(ellipse 35% 55% at 50% 58%,#7a1c3c,#e6e6e6 95%)"></div><div class="caption">Lorem ipsum dolor</div><div class="price"><s>$160.00</s>$150.00</div><div class="actions"><span><svg width="16" height="14" viewBox="0 0 16 14"><path d="M1 1 H3 L5 9 H13 L15 3 H4" fill="none" stroke="#bbb" stroke-width="1.6"/><circle cx="6" cy="12" r="1.3" fill="#bbb"/><circle cx="12" cy="12" r="1.3" fill="#bbb"/></svg></span><span><svg width="14" height="13" viewBox="0 0 14 13"><path d="M7 12 L1.5 6.5 A3 3 0 0 1 7 2.5 A3 3 0 0 1 12.5 6.5 Z" fill="#bbb"/></svg></span><span><svg width="16" height="12" viewBox="0 0 16 12"><path d="M1 3 H13 M10 0 L13 3 L10 6 M15 9 H3 M6 6 L3 9 L6 12" fill="none" stroke="#bbb" stroke-width="1.6"/></svg></span><span><svg width="14" height="14" viewBox="0 0 14 14"><circle cx="7" cy="7" r="6" fill="none" stroke="#bbb" stroke-width="1.4"/><path d="M7 4 V7 H9" fill="none" stroke="#bbb" stroke-width="1.4"/></svg></span></div></article>
    <article class="card"><div class="photo" role="img" aria-label="Model in a red top and black polka dot skirt" style="background:radial-gradient(ellipse 35% 55% at 50% 58%,#3a2a30,#e6e6e6 95%)"></div><div class="caption">Lorem ipsum dolor</div><div class="price"><s>$160.00</s>$150.00</div><div class="actions"><span><svg width="16" height="14" viewBox="0 0 16 14"><path d="M1 1 H3 L5 9 H13 L15 3 H4" fill="none" stroke="#bbb" stroke-width="1.6"/><circle cx="6" cy="12" r="1.3" fill="#bbb"/><circle cx="12" cy="12" r="1.3" fill="#bbb"/></svg></span><span><svg width="14" height="13" viewBox="0 0 14 13"><path d="M7 12 L1.5 6.5 A3 3 0 0 1 7 2.5 A3 3 0 0 1 12.5 6.5 Z" fill="#bbb"/></svg></span><span><svg width="16" height="12" viewBox="0 0 16 12"><path d="M1 3 H13 M10 0 L13 3 L10 6 M15 9 H3 M6 6 L3 9 L6 12" fill="none" stroke="#bbb" stroke-width="1.6"/></svg></span><span><svg width="14" height="14" viewBox="0 0 14 14"><circle cx="7" cy="7" r="6" fill="none" stroke="#bbb" stroke-width="1.4"/><path d="M7 4 V7 H9" fill="none" stroke="#bbb" stroke-width="1.4"/></svg></span></div></article>
    <article class="card"><div class="photo" role="img" aria-label="Model in a navy dress with yellow polka dots" style="background:radial-gradient(ellipse 35% 55% at 50% 58%,#1f2a55,#e6e6e6 95%)"></div><div class="caption">Lorem ipsum dolor</div><div class="price"><s>$160.00</s>$150.00</div><div class="actions"><span><svg width="16" height="14" viewBox="0 0 16 14"><path d="M1 1 H3 L5 9 H13 L15 3 H4" fill="none" stroke="#bbb" stroke-width="1.6"/><circle cx="6" cy="12" r="1.3" fill="#bbb"/><circle cx="12" cy="12" r="1.3" fill="#bbb"/></svg></span><span><svg width="14" height="13" viewBox="0 0 14 13"><path d="M7 12 L1.5 6.5 A3 3 0 0 1 7 2.5 A3 3 0 0 1 12.5 6.5 Z" fill="#bbb"/></svg></span><span><svg width="16" height="12" viewBox="0 0 16 12"><path d="M1 3 H13 M10 0 L13 3 L10 6 M15 9 H3 M6 6 L3 9 L6 12" fill="none" stroke="#bbb" stroke-width="1.6"/></svg></span><span><svg width="14" height="14" viewBox="0 0 14 14"><circle cx="7" cy="7" r="6" fill="none" stroke="#bbb" stroke-width="1.4"/><path d="M7 4 V7 H9" fill="none" stroke="#bbb" stroke-width="1.4"/></svg></span></div></article>
  </div>
</main>

<section class="abs community">
  <h2>BECOME PART OF OUR COMMUNITY</h2>
  <p>Sign up to our newsletter:</p>
  <div class="field"></div>
  <a class="subscribe">SUBSCRIBE</a>
  <h4>SOCIAL MEDIA:</h4>
  <div class="social" style="left:665px"><i style="background:#2d5a9a"></i>Friendloop</div>
  <div class="social" style="left:757px"><i style="background:#c8202e"></i>Pinboardly</div>
  <div class="social" style="left:850px"><i style="background:#2a7fb0"></i>Snapframe</div>
</section>

<footer class="abs footer">
  <div class="fcol" style="left:44px"><h5>MARLOWE THREADWORK</h5><ul><li>About us</li><li>Terms of use</li><li>Privacy policy</li><li>Press</li></ul></div>
  <div class="fcol" style="left:376px"><h5>CONNECT WITH US</h5><ul><li>Contact us</li><li>My Account</li><li>StyleTips</li><li>FAQs</li><li>Shipping</li><li>Track your order</li><li>Size chart</li></ul></div>
  <div class="fcol cats" style="left:696px"><h5>SHOP BY POPULAR CATEGORIES</h5><ul><li>Men</li><li>50s</li><li>Women</li><li>60s</li><li>Accessories</li><li>70s</li><li>Bags</li><li>80s</li><li>Shoes</li><li>90s</li></ul></div>
  <div class="partners">
    <span class="partner"><i style="background:#2a5aa0"></i>TrustLane</span>
    <span class="partner">PayRoute</span>
    <span class="partner" style="color:#1f4f99">WalletPass</span>
    <span class="partner" style="color:#1a2f80">Cardia</span>
    <span class="partner" style="color:#333">Orbcard</span>
  </div>
  <div class="copyright">© Marlowe Threadwork. All Prices are in AUD.</div>
</footer>

</body>
</html>
```